Orvik Lines website

i'm looking for a promotional website for my business.
we provide Rope Access, Work at Height & Difficult Access services.
we treat water leak into buildings, external renovation of buildings, windows cleaning, confined spaces services and practically jobs in which the access is difficult.
here are examples of web site i like :
http://www.layoutbazaar.example/wordpress-themes/51872.html
http://www.layoutbazaar.example/joomla-templates/51294.html

private people, commercial household chiefs, maintenance managers

Business

• - mobile friendly
- frindlo redirection
- 5 tabs
- one more customizable page - so i can add a photo and a description of the service corresponding (for now i offer 7 different services)
- contact us on each page with no redirection
- we are offering 7 different services
the website will be published in Israel which means right to left or centered for english option in the future. (logo on left hand corner)

- no flash
- should be future customisable - for future
• - a space for a slogan
- non scrollable
- photos on the landing page + redirection to gallery (photos and short films)
- 3 dynamic banners with short description of the theme of each, clicking on the banner after it opened will redirect to it's corresponding page.

```html
<!DOCTYPE html>
<html lang="en">
<head>
<meta charset="utf-8">
<title>Orvik Lines — Contacts</title>
<link rel="stylesheet" href="https://fonts.googleapis.com/css2?family=Anton&family=Noto+Sans:wght@400&display=swap">
<style>
  :root {
    --sky-light: #2f6cf0;
    --sky-deep: #0d2f86;
    --night: #05070b;
    --rock: #0b1220;
    --cyan: #00d8ff;
    --white: #ffffff;
    --black: #000000;
    --field: #3a3a3a;
    --field-text: #e6e6e6;
    --muted: #8a8f96;
    --body-text: #e8e8e8;
    --divider: #2a2f38;
    --map-base: #e8e2c8;
  }
  * { margin: 0; padding: 0; box-sizing: border-box; }
  html, body { width: 1200px; height: 595px; overflow: hidden; background: var(--night); }
  .page { position: relative; width: 1200px; height: 595px; overflow: hidden; font-family: "Noto Sans", Verdana, sans-serif; color: var(--body-text); }

  .backdrop { position: absolute; inset: 0;
    background:
      radial-gradient(ellipse 360px 420px at 1010px 330px, #131c2c 0%, rgba(11,18,32,0.6) 55%, transparent 75%),
      linear-gradient(180deg, transparent 0, transparent 142px, var(--night) 142px),
      linear-gradient(100deg, var(--sky-light) 0%, #2459d8 35%, #1a3f9e 62%, var(--sky-deep) 100%);
  }
  .backdrop-rock { position: absolute; left: 770px; top: 0; width: 430px; height: 595px;
    background: linear-gradient(160deg, rgba(20,28,44,0.95) 0%, rgba(10,14,24,0.95) 60%, rgba(5,7,11,0.9) 100%);
    border-top-left-radius: 160px 120px; }

  .brand { position: absolute; left: 22px; top: -12px; }
  .brand-name { font-family: "Anton", Impact, sans-serif; font-size: 104px; line-height: 1; color: var(--cyan); letter-spacing: 1px; }
  .brand-slogan { position: absolute; left: 149px; top: 96px; font-family: "Anton", Impact, sans-serif; font-size: 24px; color: var(--white); white-space: nowrap; }

  .main-nav { position: absolute; left: 545px; top: 59px; width: 655px; height: 51px; background: var(--black); display: flex; align-items: center; }
  .main-nav a { font-family: "Anton", Impact, sans-serif; font-size: 25px; color: var(--white); text-decoration: none; text-align: center; line-height: 51px; }
  .nav-gallery { width: 158px; }
  .nav-about { width: 133px; }
  .nav-services { width: 156px; }
  .nav-sep { color: var(--white); font-size: 18px; width: 12px; text-align: center; opacity: 0.7; }
  .main-nav a.is-current { position: absolute; right: 0; top: 0; width: 180px; height: 51px; background: var(--white); color: var(--cyan); }

  .section-title { position: absolute; font-family: "Anton", Impact, sans-serif; font-size: 25px; color: var(--white); }

  .feedback-title { left: 27px; top: 180px; }
  .field { position: absolute; left: 27px; width: 236px; height: 28px; background: var(--field); font-size: 11px; color: var(--field-text); padding: 7px 7px; }
  .field-name { top: 236px; }
  .field-email { top: 280px; }
  .field-phone { top: 324px; }
  .field-message { top: 369px; width: 312px; height: 171px; }
  .btn { position: absolute; top: 571px; height: 30px; background: var(--white); color: var(--black); font-family: "Anton", Impact, sans-serif; font-size: 17px; text-align: center; line-height: 30px; }
  .btn-clear { left: 205px; width: 62px; }
  .btn-send { left: 281px; width: 58px; }

  .column-divider { position: absolute; left: 378px; top: 187px; width: 1px; height: 408px; background: var(--divider); }

  .contact-title { left: 418px; top: 180px; }
  .map-area { position: absolute; left: 418px; top: 235px; width: 379px; height: 240px;
    background: linear-gradient(135deg, var(--map-base) 0%, #ddd6b8 55%, #b8c9d8 100%); }
  .address { position: absolute; left: 418px; top: 497px; font-size: 11px; line-height: 14px; color: var(--body-text); text-transform: uppercase; }
  .contact-lines { position: absolute; left: 418px; top: 542px; font-size: 11px; line-height: 15.5px; color: var(--muted); }
  .contact-lines span.label { display: inline-block; width: 63px; }
  .contact-lines .email-label { width: 52px; }
  .contact-lines a { color: var(--cyan); }
</style>
</head>
<body>
<div class="page">
  <div class="backdrop" role="img" aria-label="Photo of a rope-access climber silhouetted on an overhanging rock face against a blue sky"></div>
  <div class="backdrop-rock"></div>

  <header class="brand">
    <div class="brand-name">ORVIK</div>
    <div class="brand-slogan">YOUR SLOGAN</div>
  </header>

  <nav class="main-nav">
    <a class="nav-gallery" href="#">GALLERY</a>
    <span class="nav-sep">:</span>
    <a class="nav-about" href="#">ABOUT</a>
    <span class="nav-sep">:</span>
    <a class="nav-services" href="#">SERVICES</a>
    <a class="is-current" href="#">CONTACTS</a>
  </nav>

  <h2 class="section-title feedback-title">FEEDBACK</h2>
  <div class="field field-name">Name:</div>
  <div class="field field-email">E-mail:</div>
  <div class="field field-phone">Phone:</div>
  <div class="field field-message">Message:</div>
  <div class="btn btn-clear">CLEAR</div>
  <div class="btn btn-send">SEND</div>

  <div class="column-divider"></div>

  <h2 class="section-title contact-title">STAY IN TOUCH</h2>
  <div class="map-area" role="img" aria-label="Street map showing the office location"></div>
  <p class="address">118 Harbor Row Street,<br>Easton, USA E17 42KT.</p>
  <p class="contact-lines">
    <span class="label">Freephone:</span>+1 800 555 0142<br>
    <span class="label">Telephone:</span>+1 800 555 0142<br>
    <span class="label email-label">E-mail:</span><a href="#">mail@orviklines.example</a>
  </p>
</div>
</body>
</html>
```